Crime/mystery/thriller novel cover design

I am looking to get a cover designed for a novel. It is a crime/mystery/thriller set in Liverpool, England, between the 1970s and current day. I have permission to use some paintings by an artist for the cover, so it just needs put together and jazzed up. I am looking for something which has a fairly classic feel (so not just pulp airport thriller trash) but with some flair nonetheless.
The novel will be paperback, 127mm x 203mm with approx 18mm spine width. Can be gloss or matt cover, would be interesting to discuss.
The title is:
THE CASTLEMERE TIDE
Author name:
ROBERT J. KELVANSKI
Publisher:
VELUMBRA PUBLISHING LTD (or simply VELUMBRA)

I am still working on the back cover blurb but I will upload this when finished.
There are 4 images I could use for the cover though my favourite is the one called Evening, Harwick Docklands.

```html
<!DOCTYPE html>
<html lang="en">
<head>
<meta charset="utf-8">
<title>The Castlemere Tide — Cover Layout</title>
<link rel="stylesheet" href="https://fonts.googleapis.com/css2?family=Oswald:wght@500;700&family=Barlow:wght@400&family=Barlow+Semi+Condensed:wght@300&display=swap">
<style>
  :root {
    --page: #ffffff;
    --ink: #111111;
    --cover-text: #ffffff;
    --teal: #1d3a38;
    --green: #3f5a2c;
    --amber: #c98a2a;
    --orange: #b5541d;
    --navy: #0b1224;
    --blue: #1c2e6b;
    --night: #0c0d0c;
  }
  * { box-sizing: border-box; margin: 0; padding: 0; }
  html, body {
    width: 1200px; height: 1200px; overflow: hidden;
    background: var(--page);
  }
  .canvas { position: relative; width: 1200px; height: 1200px; }

  .era-label {
    position: absolute; left: 292px; transform: translateX(-50%);
    font-family: "Barlow", sans-serif; font-size: 17px; letter-spacing: 1.2px;
    color: var(--ink); white-space: nowrap;
  }
  .era-label--top { top: 118px; }
  .era-label--bottom { top: 1038px; }
  .leader { position: absolute; left: 285px; width: 1px; background: var(--ink); }
  .leader--top { top: 157px; height: 60px; }
  .leader--bottom { top: 978px; height: 60px; }

  .panel { position: absolute; top: 236px; height: 735px; overflow: hidden; color: var(--cover-text); }
  .front { left: 62px; width: 461px; }
  .spine { left: 571px; width: 64px; }
  .back { left: 684px; width: 461px; }

  .artwork { position: absolute; inset: 0; }
  .front .artwork {
    background: linear-gradient(180deg,
      var(--teal) 0%, var(--green) 14%, #7c7a3a 24%, var(--amber) 33%,
      #6a4a2c 44%, #2a2a30 54%, var(--navy) 64%, #1a1f3a 74%,
      var(--orange) 84%, #4a2a40 92%, var(--blue) 100%);
  }
  .spine .artwork {
    background: linear-gradient(180deg,
      #0f1a22 0%, #142230 50%, #1d2a4a 62%, #8a5a2a 70%,
      var(--amber) 74%, var(--blue) 84%, #10194a 100%);
  }
  .back .artwork {
    background:
      radial-gradient(ellipse 70% 22% at 60% 62%, rgba(201,160,42,.55), transparent 70%),
      linear-gradient(180deg, var(--night) 0%, #1a1f1a 30%, #2a2a1c 52%,
        #4a3a14 62%, #141210 72%, #5a2f14 86%, var(--orange) 100%);
  }
  .back .artwork::after { content: ""; position: absolute; inset: 0; background: rgba(0,0,0,.35); }

  .display { font-family: "Oswald", sans-serif; font-weight: 700; text-transform: uppercase; line-height: 1; white-space: nowrap; }
  .spaced { font-family: "Oswald", sans-serif; font-weight: 500; text-transform: uppercase; line-height: 1; white-space: nowrap; }
  .center { position: absolute; left: 0; right: 0; text-align: center; }

  .front__author { top: 22px; font-size: 17px; letter-spacing: 11px; padding-left: 11px; }
  .front__the { top: 326px; font-size: 22px; letter-spacing: 17px; padding-left: 17px; }
  .front__title { top: 352px; font-size: 76px; letter-spacing: -0.5px; }
  .front__tide { top: 453px; font-size: 36px; letter-spacing: 42px; padding-left: 42px; }
  .front__publisher {
    position: absolute; right: 24px; top: 707px; font-size: 11px; letter-spacing: 2.2px;
  }

  .spine__text {
    position: absolute; top: 40px; left: 0; width: 64px;
    writing-mode: vertical-rl; display: flex; align-items: center;
  }
  .spine__the { font-size: 10px; letter-spacing: 9px; margin-bottom: 6px; }
  .spine__title { font-size: 40px; }
  .spine__tide { font-size: 22px; letter-spacing: 16px; margin-top: 14px; }
  .spine__author {
    position: absolute; bottom: 24px; left: 0; width: 64px;
    writing-mode: vertical-rl; display: flex; align-items: center;
    font-size: 9px; letter-spacing: 3.2px;
  }

  .back__the { top: 59px; font-size: 13px; letter-spacing: 9px; padding-left: 9px; }
  .back__title { top: 74px; font-size: 44px; }
  .back__tide { top: 126px; font-size: 21px; letter-spacing: 22px; padding-left: 22px; }
  .back__blurb {
    position: absolute; left: 60px; top: 196px; width: 336px;
    font-family: "Barlow Semi Condensed", sans-serif; font-weight: 300;
    font-size: 9.8px; line-height: 17.6px; text-align: justify; hyphens: auto;
  }
  .back__portrait {
    position: absolute; left: 60px; top: 533px; width: 134px; height: 134px;
    border-radius: 50%; background: var(--cover-text);
  }
  .back__credit { position: absolute; left: 212px; top: 568px; }
  .back__author { font-size: 18px; letter-spacing: 1.4px; }
  .back__role { font-size: 9.5px; letter-spacing: 2.6px; margin-top: 7px; }
  .back__publisher { font-size: 8.5px; letter-spacing: 3px; margin-top: 22px; }
</style>
</head>
<body>
<main class="canvas">
  <p class="era-label era-label--top">1970 Liverpool</p>
  <span class="leader leader--top"></span>

  <section class="panel front">
    <div class="artwork" role="img" aria-label="Painting: Evening, Harwick Docklands — waterfront skyline under a stormy amber sky reflected upside down in the river"></div>
    <p class="center spaced front__author">Robert J. Kelvanski</p>
    <p class="center spaced front__the">The</p>
    <h1 class="center display front__title">Castlemere</h1>
    <p class="center spaced front__tide">Tide</p>
    <p class="spaced front__publisher">Velumbra Publishing Ltd</p>
  </section>

  <section class="panel spine">
    <div class="artwork" role="img" aria-label="Continuation of the docklands painting across the spine"></div>
    <div class="spine__text">
      <span class="spaced spine__the">The</span>
      <span class="display spine__title">Castlemere</span>
      <span class="spaced spine__tide">Tide</span>
    </div>
    <p class="spaced spine__author">Robert J. Kelvanski</p>
  </section>

  <section class="panel back">
    <div class="artwork" role="img" aria-label="Darkened waterfront skyline silhouette against a yellow sunset with rust-orange reflections"></div>
    <p class="center spaced back__the">The</p>
    <h2 class="center display back__title">Castlemere</h2>
    <p class="center spaced back__tide">Tide</p>
    <p class="back__blurb">Lorem ipsum dolor sit amet, consectetur adipiscing elit, sed do eiusmod tempor incididunt ut labore et dolore magna aliqua. Quis ipsum suspendisse ultrices gravida. Risus commodo viverra maecenas accumsan lacus vel facilisis. Lorem ipsum dolor sit amet, consectetur adipiscing elit, sed do eiusmod tempor incididunt ut labore et dolore magna aliqua. Quis ipsum suspendisse ultrices gravida. Risus commodo viverra maecenas accumsan lacus vel facilisis. Lorem ipsum dolor sit amet, consectetur adipiscing elit, sed do eiusmod tempor incididunt ut labore et dolore magna aliqua. Quis ipsum suspendisse ultrices gravida. Risus commodo viverra maecenas accumsan lacus vel facilisis. Lorem ipsum dolor sit amet, consectetur adipiscing elit, sed do eiusmod tempor incididunt ut labore et dolore magna aliqua. Quis ipsum suspendisse ultrices gravida. Risus commodo viverra maecenas accumsan lacus vel facilisis. Lorem ipsum dolor sit amet, consectetur adipiscing elit, sed do eiusmod tempor incididunt ut labore et dolore magna aliqua. Quis ipsum suspendisse ultrices gravida. Risus commodo viverra maecenas accumsan lacus vel facilisis. Lorem ipsum dolor sit amet, consectetur adipiscing elit, sed do eiusmod tempor incididunt ut labore et dolore magna aliqua. Quis ipsum suspendisse ultrices gravida. Risus commodo viverra maecenas accumsan lacus vel facilisis.</p>
    <div class="back__portrait" role="img" aria-label="Author portrait placeholder"></div>
    <div class="back__credit">
      <p class="display back__author">Robert J. Kelvanski</p>
      <p class="spaced back__role">Author</p>
      <p class="spaced back__publisher">Velumbra Publishing Ltd</p>
    </div>
  </section>

  <span class="leader leader--bottom"></span>
  <p class="era-label era-label--bottom">Modern Day Liverpool</p>
</main>
</body>
</html>
```